Bright Path Flyer Design for Virtual Online Clinic. -5.5 x 8.5 inches (half sheet)

We need a clean, modern flyer design for Bright Path, a new virtual walk-in clinic based in British Columbia. The flyer will be used in libraries, pharmacies, and community centers to help residents easily access primary care through their Bright Path NFC access card.
The flyer will ask a question : NEED A DOCTOR? This should be large and attention grabbing.
The design should clearly feature a Bright Path card image (the access card) as the centerpiece and visually show how patients can use it to book appointments. The tone should feel trustworthy, healthcare-oriented, and community-friendly — clean fonts, clear spacing, and strong readability from a distance.

Side One: This card has the NFC Access Card.
NEED A DOCTOR? (Large Font, Attention Grabbing)
How to Book an Appointment using your Bright Path Card
Step 1: Tap Your Card on Your Phone
Hold your card near the back of your phone.
It will activate automatically — no app needed.
The Bright Path scheduler will open.
Step 2: Schedule Your Appointment
Select your clinical concern.
Choose your time window.
Register (only once).
Confirm your appointment.
Step 3: Relax, we’ll take care of the rest
A doctor will call during your scheduled time.
Once booked, you’ll be able to call our office.
No emails, no texts — just a real person.
It’s that simple.
Side Two:
About Bright Path
Created by Dr. Marcus Ferrigan
Bright Path was founded to make healthcare simple and convenient. Prescription renewals. Common infections. Medical notes. And so much more.
Our doctors can address 120+ health concerns virtually — providing quality care without the waiting room. No waiting rooms. Just real doctors providing real care.
Why Patients Choose Bright Path
Easy access – book and be seen from anywhere in BC.
Effortless booking – tap your Bright Path Card to begin.
Trusted physicians – every visit is with a licensed BC family doctor.
How It Works
Book your visit — choose a time window that fits your day.
Join the queue — you’ll be called when it’s your turn.
Speak directly with your doctor — simple, secure, and stress-free.
Convenient Care for Common Concerns

Additional Details.
Please find the domain to be launched soon. I've attached the NFC card file for review, it is 85.5 mm x 54 mm. The card will be glued to the flyer.
I've attached examples of flyers but they are not the look I am seeking and I am looking for creative solutions.
Thank you!
http://brightpath-example.test/

Adult Patients in British Columbia

Healthcare

• Looking for clean lines, uniform appearance, and high legibility i.e poppins

0054AA
0677BA
7BADD7
CADEEF
E8F1F8

• Need A Doctor?
• Elegant style, not too busy, clear layout.
• Clutter, look cheap - review examples.

```html
<!DOCTYPE html>
<html lang="en">
<head>
<meta charset="utf-8">
<title>Bright Path – Need a Doctor? Flyer</title>
<link rel="stylesheet" href="https://fonts.googleapis.com/css2?family=Poppins:wght@400;600;700;800&family=Roboto+Condensed:wght@400;500;600&family=Rubik:wght@400&display=swap">
<style>
  :root{
    --navy:#2d438b;
    --navy-deep:#243a7e;
    --accent:#0677ba;
    --sky:#7badd7;
    --mist:#cadeef;
    --ice:#e8f1f8;
    --slate:#6b7382;
    --grey-text:#6e6e73;
    --green:#14bf7b;
    --white:#ffffff;
    --stage:#d6d6d6;
  }
  *{box-sizing:border-box;margin:0;padding:0}
  html,body{width:1200px;height:890px;overflow:hidden;background:var(--stage)}
  body{position:relative;font-family:'Poppins',sans-serif}
  .flyer{position:absolute;top:93px;width:460px;height:709px;background:var(--white);overflow:hidden}
  .flyer--front{left:105px}
  .flyer--back{left:641px}
  .abs{position:absolute}
  .wave{position:absolute;left:0;top:0}
  .photo{position:absolute}
  .brand{font-family:'Poppins',sans-serif;font-weight:600;color:var(--white);white-space:nowrap}

  /* front */
  .front-brand{left:24px;top:46px;font-size:32px}
  .nfc-note{left:25px;top:112px;font-family:'Roboto Condensed',sans-serif;font-weight:600;font-size:16px;color:var(--white)}
  .headline{left:22px;top:140px;color:var(--white);font-weight:800;line-height:1}
  .headline .big{display:block;font-size:56px;letter-spacing:-1px}
  .headline .sub{display:block;font-size:40px;margin-top:2px}
  .booking-title{left:35px;top:306px;font-size:26.5px;font-weight:700;color:var(--navy);line-height:1.05}
  .card-frame{left:88px;top:408px;width:294px;height:168px}
  .access-card{left:94px;top:415px;width:280px;height:154px;border:1px solid var(--navy);background:var(--white);overflow:hidden}
  .access-card .card-brand{position:absolute;left:104px;top:62px;font-size:24px;font-weight:600;color:var(--navy)}
  .access-card .tap{position:absolute;right:16px;bottom:14px;display:flex;align-items:center;gap:6px;font-family:'Rubik',sans-serif;font-size:8px;color:var(--navy)}
  .steps{left:22px;top:584px;width:420px;height:100px}
  .step{position:absolute;top:0}
  .step h3{font-size:22px;font-weight:700;color:var(--grey-text);line-height:1}
  .step ul{list-style:none;margin-top:8px}
  .step li{display:flex;align-items:center;gap:4px;font-family:'Roboto Condensed',sans-serif;font-size:6.8px;color:var(--navy);height:14px;white-space:nowrap}
  .step li em{font-style:normal;color:var(--green)}
  .step li svg{flex:none}
  .divider{position:absolute;top:30px;height:70px;border-left:1px dashed var(--navy)}
  .footer{position:absolute;left:0;width:460px;background:var(--navy);color:var(--white);font-family:'Rubik',sans-serif;font-size:9px;letter-spacing:.6px;display:flex;align-items:center;justify-content:center}
  .flyer--front .footer{top:690px;height:19px}

  /* back */
  .about-title{left:236px;top:22px;font-size:28px;font-weight:800;color:var(--white)}
  .back-brand{left:222px;top:58px;font-size:30px}
  .about-copy{left:223px;top:116px;width:222px;font-family:'Rubik',sans-serif;font-size:9.3px;line-height:1.27;color:var(--white)}
  .about-copy p+p{margin-top:6px}
  .info-panel{left:27px;top:363px;width:405px;height:242px;border-radius:14px;overflow:hidden;display:flex}
  .info-col{padding:14px 16px 0 17px;color:var(--white)}
  .info-col--why{width:205px;background:var(--navy)}
  .info-col--how{flex:1;background:var(--slate);padding-left:12px}
  .info-col h2{font-size:15.5px;font-weight:700;line-height:1.3;margin-bottom:16px}
  .info-col--how h2{font-size:19.5px;margin-bottom:28px;margin-top:2px}
  .info-list{list-style:none;font-family:'Roboto Condensed',sans-serif}
  .info-list li{display:flex;gap:8px;margin-bottom:10px}
  .info-list li svg{flex:none;margin-top:3px}
  .info-list strong{display:block;font-weight:400;font-size:15px;line-height:1}
  .info-list span{display:block;font-size:10.5px;line-height:1.25;margin-top:2px}
  .cta-pill{left:92px;top:577px;width:275px;height:58px;border-radius:29px;background:var(--green);color:var(--white);font-weight:800;font-size:16.5px;line-height:1.05;text-align:center;display:flex;align-items:center;justify-content:center}
  .call{left:0;width:460px;top:646px;display:flex;justify-content:center;align-items:center;gap:8px;font-weight:700;font-size:18px}
  .call .label{color:var(--grey-text)}
  .call .number{color:var(--navy)}
  .flyer--back .footer{top:681px;height:28px}
</style>
</head>
<body>

<!-- FRONT -->
<section class="flyer flyer--front" aria-label="Flyer front">
  <svg class="wave" width="460" height="340" viewBox="0 0 460 340" aria-hidden="true">
    <path d="M0 0H460V225C420 290 350 325 272 322C170 318 110 256 0 258Z" fill="var(--navy)"/>
  </svg>
  <div class="photo" role="img" aria-label="Smiling female doctor in a white coat with a stethoscope, pointing up" style="left:245px;top:36px;width:205px;height:290px;background:linear-gradient(180deg,#4b62a8 0%,#c9d6ea 45%,#e6ecf5 100%);border-radius:90px 90px 0 0"></div>
  <svg class="wave" width="460" height="340" viewBox="0 0 460 340" aria-hidden="true">
    <path d="M0 258C110 256 170 318 272 322C350 325 420 290 460 225V340H0Z" fill="var(--white)"/>
    <path d="M0 258C110 256 170 318 272 322C350 325 420 290 460 225" fill="none" stroke="var(--accent)" stroke-width="5"/>
  </svg>

  <div class="abs brand front-brand">Bright Path</div>
  <div class="abs nfc-note">This card has the NFC Access Card.</div>
  <h1 class="abs headline"><span class="big">NEED</span><span class="sub">A DOCTOR?</span></h1>

  <h2 class="abs booking-title">How to Book<br>an Appointment using your<br>Bright Path Card</h2>

  <svg class="abs card-frame" viewBox="0 0 294 168" aria-hidden="true">
    <path d="M0 14V0H14M280 0H294V14M294 154V168H280M14 168H0V154" fill="none" stroke="var(--navy)" stroke-width="1.3"/>
  </svg>
  <div class="abs access-card" aria-label="Bright Path NFC access card">
    <svg class="abs" width="280" height="154" viewBox="0 0 280 154" style="left:0;top:0" aria-hidden="true">
      <path d="M0 0H120C90 30 70 70 68 100C66 125 70 140 75 154H0Z" fill="var(--navy)"/>
      <rect x="255" y="12" width="11" height="11" rx="1" fill="none" stroke="var(--navy)" stroke-width="1.4"/>
    </svg>
    <div class="card-brand">Bright Path</div>
    <div class="tap">Tap Here to Book
      <svg width="22" height="13" viewBox="0 0 22 13" aria-hidden="true">
        <rect x=".5" y=".5" width="21" height="12" rx="2" fill="none" stroke="var(--navy)"/>
        <rect x="3" y="4" width="5" height="5" fill="var(--navy)"/>
        <path d="M11 4q2 2.5 0 5M14 3q3 3.5 0 7M17 2q4 4.5 0 9" fill="none" stroke="var(--navy)"/>
      </svg>
    </div>
  </div>

  <div class="abs steps">
    <div class="step" style="left:0">
      <h3>Step 1:</h3>
      <ul>
        <li><svg width="9" height="9" viewBox="0 0 10 10"><rect x="1" y="1" width="6" height="8" rx="1" fill="none" stroke="var(--navy)"/></svg>Tap Your Card on Your Phone</li>
        <li><svg width="9" height="9" viewBox="0 0 10 10"><rect x="2" y="1" width="6" height="8" rx="1" fill="none" stroke="var(--navy)"/></svg>Hold your card near the back of your phone.</li>
        <li><svg width="9" height="9" viewBox="0 0 10 10"><circle cx="5" cy="5" r="4" fill="none" stroke="var(--navy)"/></svg>It will activate automatically – <em>no app needed.</em></li>
        <li><svg width="9" height="9" viewBox="0 0 10 10"><rect x="2" y="1" width="6" height="8" rx="1" fill="none" stroke="var(--navy)"/></svg>The Bright Path scheduler will open.</li>
      </ul>
    </div>
    <div class="divider" style="left:150px"></div>
    <div class="step" style="left:163px">
      <h3>Step 2</h3>
      <ul>
        <li><svg width="9" height="9" viewBox="0 0 10 10"><rect x="1" y="2" width="8" height="7" fill="none" stroke="var(--navy)"/></svg>Schedule Your Appointment</li>
        <li><svg width="9" height="9" viewBox="0 0 10 10"><circle cx="5" cy="5" r="4" fill="none" stroke="var(--navy)"/><path d="M3 5l1.5 1.5L7 4" fill="none" stroke="var(--navy)"/></svg>Select your clinical concern.</li>
        <li><svg width="9" height="9" viewBox="0 0 10 10"><circle cx="5" cy="5" r="4" fill="none" stroke="var(--navy)"/><path d="M5 3v2l1.5 1" fill="none" stroke="var(--navy)"/></svg>Choose your time window.</li>
        <li><svg width="9" height="9" viewBox="0 0 10 10"><rect x="1" y="1" width="8" height="8" fill="none" stroke="var(--navy)"/></svg>Register <em>(only once).</em></li>
        <li><svg width="9" height="9" viewBox="0 0 10 10"><circle cx="5" cy="5" r="4" fill="none" stroke="var(--navy)"/><path d="M3 5l1.5 1.5L7 4" fill="none" stroke="var(--navy)"/></svg>Confirm your appointment.</li>
      </ul>
    </div>
    <div class="divider" style="left:268px"></div>
    <div class="step" style="left:283px">
      <h3>Step 3</h3>
      <ul>
        <li><svg width="9" height="9" viewBox="0 0 10 10"><circle cx="5" cy="5" r="4" fill="none" stroke="var(--green)"/><path d="M3 5l1.5 1.5L7 4" fill="none" stroke="var(--green)"/></svg>Relax, we'll take care of the rest</li>
        <li><svg width="9" height="9" viewBox="0 0 10 10"><circle cx="5" cy="5" r="4" fill="none" stroke="var(--green)"/><path d="M3 5l1.5 1.5L7 4" fill="none" stroke="var(--green)"/></svg>A doctor will call during your scheduled time.</li>
        <li><svg width="9" height="9" viewBox="0 0 10 10"><circle cx="5" cy="5" r="4" fill="none" stroke="var(--green)"/><path d="M3 5l1.5 1.5L7 4" fill="none" stroke="var(--green)"/></svg>Once booked, you'll be able to call our office.</li>
        <li><svg width="9" height="9" viewBox="0 0 10 10"><circle cx="5" cy="5" r="4" fill="none" stroke="var(--green)"/><path d="M3 5l1.5 1.5L7 4" fill="none" stroke="var(--green)"/></svg>No emails, no texts – <em>just a real person.</em></li>
        <li><svg width="9" height="9" viewBox="0 0 10 10"><circle cx="5" cy="5" r="4" fill="none" stroke="var(--green)"/><path d="M3 5l1.5 1.5L7 4" fill="none" stroke="var(--green)"/></svg>It's that simple.</li>
      </ul>
    </div>
  </div>

  <div class="footer">www.brightpath-example.test</div>
</section>

<!-- BACK -->
<section class="flyer flyer--back" aria-label="Flyer back">
  <svg class="wave" width="460" height="330" viewBox="0 0 460 330" aria-hidden="true">
    <path d="M0 0H460V247C380 232 300 260 168 303C90 328 40 290 0 231Z" fill="var(--navy)"/>
    <path d="M0 231C40 290 90 328 168 303C300 260 380 232 460 247" fill="none" stroke="var(--accent)" stroke-width="5"/>
  </svg>

  <div class="abs" style="left:46px;top:26px;width:157px;height:312px;border-radius:20px;background:#2a2f33"></div>
  <div class="photo" role="img" aria-label="Smiling male doctor in a white coat holding a clipboard, shown on a phone screen" style="left:55px;top:35px;width:139px;height:294px;border-radius:14px;background:linear-gradient(180deg,#d7d9db 0%,#c9ccd0 40%,#eef1f4 100%)"></div>

  <div class="abs about-title">About</div>
  <div class="abs brand back-brand">Bright Path</div>
  <div class="abs about-copy">
    <p>Created by Dr. Marcus Ferrigan<br>Bright Path was founded to make healthcare simple and convenient. Prescription renewals. Common infections. Medical notes. And so much more.</p>
    <p>Our doctors can address 120+ health concerns virtually — providing quality care without the waiting room. No waiting rooms. Just real doctors providing real care.</p>
  </div>

  <div class="abs info-panel">
    <div class="info-col info-col--why">
      <h2>Why Patients<br>Choose Bright Path</h2>
      <ul class="info-list">
        <li><svg width="15" height="15" viewBox="0 0 16 16"><rect x="1" y="1" width="14" height="14" rx="2" fill="none" stroke="#fff" stroke-width="1.3"/><path d="M5 11l6-6M8 5h3v3" fill="none" stroke="#fff" stroke-width="1.3"/></svg><div><strong>Easy access –</strong><span>Book and be seen from anywhere in BC.</span></div></li>
        <li><svg width="15" height="15" viewBox="0 0 16 16"><rect x="1" y="2" width="14" height="13" rx="2" fill="none" stroke="#fff" stroke-width="1.3"/><path d="M1 6h14M5 10l2 2 4-4" fill="none" stroke="#fff" stroke-width="1.3"/></svg><div><strong>Effortless booking –</strong><span>Tap your Bright Path Card to begin.</span></div></li>
        <li><svg width="15" height="15" viewBox="0 0 16 16"><path d="M8 1l6 2v5c0 4-3 6-6 7-3-1-6-3-6-7V3z" fill="none" stroke="#fff" stroke-width="1.3"/><path d="M5 8l2 2 4-4" fill="none" stroke="#fff" stroke-width="1.3"/></svg><div><strong>Trusted physicians –</strong><span>Every visit is with a licensed BC<br>family doctor.</span></div></li>
      </ul>
    </div>
    <div class="info-col info-col--how">
      <h2>How It Works</h2>
      <ul class="info-list">
        <li><svg width="13" height="13" viewBox="0 0 14 14"><circle cx="7" cy="7" r="6" fill="none" stroke="var(--green)" stroke-width="1.3"/><path d="M4 7l2 2 4-4" fill="none" stroke="var(--green)" stroke-width="1.3"/></svg><div><strong>Book your visit –</strong><span>Choose a time window that fits your day.</span></div></li>
        <li><svg width="13" height="13" viewBox="0 0 14 14"><circle cx="7" cy="7" r="6" fill="none" stroke="var(--green)" stroke-width="1.3"/><path d="M4 7l2 2 4-4" fill="none" stroke="var(--green)" stroke-width="1.3"/></svg><div><strong>Join the queue –</strong><span>You'll be called when it's your turn.</span></div></li>
        <li><svg width="13" height="13" viewBox="0 0 14 14"><circle cx="7" cy="7" r="6" fill="none" stroke="var(--green)" stroke-width="1.3"/><path d="M4 7l2 2 4-4" fill="none" stroke="var(--green)" stroke-width="1.3"/></svg><div><strong>Speak directly with<br>your doctor –</strong><span>Simple, secure, and stress-free.</span></div></li>
      </ul>
    </div>
  </div>

  <div class="abs cta-pill">CONVENIENT CARE<br>FOR COMMON CONCERNS</div>

  <div class="abs call">
    <span class="label">CALL US TODAY</span>
    <svg width="20" height="20" viewBox="0 0 20 20" aria-hidden="true"><circle cx="10" cy="10" r="8.5" fill="none" stroke="var(--green)" stroke-width="1.6"/><path d="M7 5.5l1.5 2.5-1 1c.6 1.4 1.6 2.4 3 3l1-1 2.5 1.5-.8 1.6c-3.5 0-7.5-4-7.5-7.5z" fill="var(--green)"/></svg>
    <span class="number">555-014-2290</span>
  </div>

  <div class="footer">www.brightpath-example.test</div>
</section>

</body>
</html>
```